New Website Design. Porjtect is Guaranteed.

I would like a site similar to this: http://givevanrelief.org.

old site: http://www.wheelsfordreams.org

Create a professional website; a car donation site seeking leads to return calls.

Please see http://givevanrelief.org for the concept I am after.

The webpage should have a professional feel. The pages to include are 'Home', 'About us' and 'Get Started'

Industry/Entity Type

It Professional

Coding

Coded - Design and coding required

Number of Pages Required

1 page

```html
<!DOCTYPE html>
<html lang="en">
<head>
<meta charset="utf-8">
<title>Open Road Giving – Donate Your Car</title>
<link href="https://fonts.googleapis.com/css2?family=Roboto+Slab:wght@400;700&family=Roboto:wght@400;500;700&display=swap" rel="stylesheet">
<style>
:root{
  --blue:#1b55a6;
  --red:#c3170f;
  --red-deep:#b5130c;
  --dark:#2b2b2b;
  --grey-text:#6b6b6b;
  --soft-bg:#f4f5f7;
  --white:#ffffff;
}
*{margin:0;padding:0;box-sizing:border-box}
html,body{width:809px;height:1200px;overflow:hidden;background:var(--white)}
body{position:relative;font-family:'Roboto',Arial,sans-serif}
.abs{position:absolute}

/* header */
.brand{left:58px;top:30px;display:flex;align-items:center;gap:8px}
.brand-mark{width:12px;height:12px;background:var(--blue)}
.brand-name{font-family:'Roboto',Arial,sans-serif;font-weight:500;font-size:20px;color:var(--blue);letter-spacing:.2px}
.nav{left:0;top:81px;width:809px;height:33px;background:var(--blue)}
.nav a{position:absolute;top:12px;color:var(--white);font-size:8.5px;font-weight:500;text-decoration:none;letter-spacing:.2px}

/* hero */
.hero{left:0;top:114px;width:809px;height:249px;
  background:linear-gradient(100deg,#3a4250 0%,#6d7684 28%,#bfc3c8 50%,#d9d6d3 70%,#c9b6a8 100%)}

/* donation panel */
.panel{left:535px;top:13px;width:216px;height:328px}
.panel-head{left:535px;top:38px;width:216px;text-align:center;color:var(--white)}
.panel-head .call{font-size:13px;letter-spacing:.3px}
.panel-head .phone{font-family:'Roboto Slab',Georgia,serif;font-weight:700;font-size:17px;margin-top:3px}
.form-title{left:535px;top:81px;width:216px;height:33px;background:#c91d17;color:var(--white);
  font-family:'Roboto Slab',Georgia,serif;font-size:14px;text-align:center;line-height:33px}
.field{height:24px;background:var(--white);border-radius:2px;font-size:8px;color:#555;padding-left:8px;line-height:24px}
.submit{left:547px;top:288px;width:193px;height:27px;background:var(--dark);color:var(--white);
  font-size:9.5px;font-weight:700;text-align:center;line-height:27px;border-radius:2px}

/* features */
.feature-icon{width:57px;height:57px;border-radius:50%;display:flex;align-items:center;justify-content:center}
.feature-title{font-family:'Roboto Slab',Georgia,serif;font-size:13px}
.feature-text{font-size:7.6px;color:var(--grey-text);line-height:16.5px;width:150px}

/* donate section */
.donate{left:0;top:516px;width:809px;height:274px;background:var(--soft-bg)}
.car-photo{left:0;top:516px;width:300px;height:274px;
  background:radial-gradient(ellipse at 40% 55%,#8a8d91 0%,#b9bcc0 45%,#eceef0 80%,var(--soft-bg) 100%)}
.donate h2{font-family:'Roboto Slab',Georgia,serif;font-weight:400;font-size:17.5px;color:var(--blue)}
.donate-intro{font-size:7.8px;color:#555;line-height:15px;width:410px}
.step-num{width:21px;height:21px;border-radius:50%;background:var(--blue);border:2px solid #d6e0ee;
  color:var(--white);font-size:7px;font-weight:700;text-align:center;line-height:17px}
.step-text{font-size:8.2px;color:#666;line-height:16px;width:360px}
.step-text b{font-family:'Roboto Slab',Georgia,serif;color:#333;font-size:9.5px}

/* red band */
.band{left:0;top:790px;width:809px;height:210px;background:linear-gradient(90deg,var(--red-deep),#c81f17 50%,var(--red-deep))}
.perk-label{font-family:'Roboto Slab',Georgia,serif;font-size:11.5px;color:var(--white);text-align:center;width:140px;line-height:16px}

/* thanks */
.thanks{left:0;top:1000px;width:809px;height:158px;background:#f6f7f9;text-align:center}
.thanks h3{font-family:'Roboto Slab',Georgia,serif;font-weight:400;font-size:17.5px;color:var(--blue);margin-top:41px}
.thanks p{font-size:8.6px;color:#666;margin-top:10px}
.thanks .toll{font-family:'Roboto Slab',Georgia,serif;font-size:15px;color:var(--red);margin-top:9px}

/* footer */
.footer{left:0;top:1158px;width:809px;height:42px;background:var(--blue)}
.copyright{left:58px;top:17px;font-size:8.6px;color:var(--white)}
.social{top:9px;width:24px;height:24px;border:1.5px solid var(--white);border-radius:50%}
</style>
</head>
<body>

<header>
  <div class="abs brand"><span class="brand-mark"></span><span class="brand-name">Open Road Giving</span></div>
  <nav class="abs nav">
    <a style="left:84px">HOME</a>
    <a style="left:143px">ABOUT US</a>
    <a style="left:217px">SERVICES</a>
    <a style="left:292px">HOW IT WORKS</a>
    <a style="left:389px">CHARITIES</a>
    <a style="left:465px">CONTACT US</a>
  </nav>
</header>

<section class="abs hero" role="img" aria-label="Photo of a hand holding out car keys in front of a car"></section>

<aside>
  <svg class="abs panel" viewBox="0 0 216 328" aria-hidden="true">
    <polygon points="0,0 108,17 216,0 216,328 0,328" fill="var(--red)"/>
  </svg>
  <div class="abs panel-head">
    <div class="call">CALL TODAY TO DONATE</div>
    <div class="phone">1-800-555-0147</div>
  </div>
  <div class="abs form-title">Donation Pick Up Form</div>
  <div class="abs field" style="left:547px;top:129px;width:94px">First Name :</div>
  <div class="abs field" style="left:647px;top:129px;width:94px">Last Name :</div>
  <div class="abs field" style="left:547px;top:158px;width:192px">Email :</div>
  <div class="abs field" style="left:547px;top:188px;width:192px">Phone :</div>
  <div class="abs field" style="left:547px;top:218px;width:94px">Zip Code :</div>
  <div class="abs field" style="left:647px;top:218px;width:94px">Year of Vehicle :</div>
  <div class="abs field" style="left:547px;top:249px;width:94px">Make of Vehicle :</div>
  <div class="abs field" style="left:647px;top:249px;width:94px">Model of Vehicle :</div>
  <div class="abs submit">SUBMIT APPLICATION</div>
</aside>

<section class="features">
  <div class="abs feature-icon" style="left:58px;top:405px;background:var(--blue)">
    <svg width="30" height="26" viewBox="0 0 30 26"><path d="M3 9 Q15 0 27 9 L24 12 L20 9 L10 9 L6 12 Z" fill="#fff"/><rect x="6" y="12" width="18" height="12" rx="2" fill="#fff"/><g fill="var(--blue)"><circle cx="11" cy="16" r="1.2"/><circle cx="15" cy="16" r="1.2"/><circle cx="19" cy="16" r="1.2"/><circle cx="11" cy="20" r="1.2"/><circle cx="15" cy="20" r="1.2"/><circle cx="19" cy="20" r="1.2"/></g></svg>
  </div>
  <div class="abs feature-title" style="left:129px;top:403px;color:var(--blue)">Call Us</div>
  <div class="abs feature-text" style="left:129px;top:426px">We issue you an IRS tax receipt &amp; offer the largest resale network to get you the highest tax write-off possible</div>

  <div class="abs feature-icon" style="left:297px;top:405px;background:var(--red)">
    <svg width="32" height="28" viewBox="0 0 32 28" fill="none" stroke="#fff" stroke-width="2.2"><path d="M3 20 V12 H12 L14 7 H19 V20 Z" fill="#fff"/><path d="M17 8 L27 2 V9"/><circle cx="8" cy="21" r="3.5" fill="var(--red)"/><circle cx="18" cy="21" r="3.5" fill="var(--red)"/></svg>
  </div>
  <div class="abs feature-title" style="left:368px;top:403px;color:var(--red)">We Tow It</div>
  <div class="abs feature-text" style="left:368px;top:426px">We issue you an IRS tax receipt &amp; offer the largest resale network to get you the highest tax write-off possible</div>

  <div class="abs feature-icon" style="left:536px;top:405px;background:var(--blue)">
    <span style="color:#fff;font-size:30px;font-weight:700">%</span>
  </div>
  <div class="abs feature-title" style="left:607px;top:403px;color:var(--blue)">Tax Write Off</div>
  <div class="abs feature-text" style="left:607px;top:426px">We issue you an IRS tax receipt &amp; offer the largest resale network to get you the highest tax write-off possible</div>
</section>

<section class="abs donate">
  <h2 class="abs" style="left:338px;top:17px">Donate Car to Charity!</h2>
  <p class="abs donate-intro" style="left:338px;top:47px">Complete the form and a representative will call you to arrange a convenient time to pickup your car.And benefit Hometown Veterans Aid Fund. An IRS 501(c)3 nonprofit organization.</p>
  <div class="abs step-num" style="left:339px;top:95px">01</div>
  <p class="abs step-text" style="left:380px;top:97px"><b>FREE LOCAL TOWING</b> : Free 24/7 Pickup with No DMV Hassles.</p>
  <div class="abs step-num" style="left:339px;top:130px">02</div>
  <p class="abs step-text" style="left:380px;top:131px"><b>FAST PICKUP</b> : Same Day to 24 Hours.</p>
  <div class="abs step-num" style="left:339px;top:165px">03</div>
  <p class="abs step-text" style="left:380px;top:166px"><b>INCOME TAX DEDUCTION</b> : We issue you an IRS tax receipt &amp; offer the largest resale network to get you the highest tax write-off possible.</p>
  <div class="abs step-num" style="left:339px;top:212px">04</div>
  <p class="abs step-text" style="left:380px;top:213px"><b>NO PAPERWORK HASSLES</b> : We take any car and handle everything:DMV, Smog, &amp; IRS paperwork.</p>
</section>
<div class="abs car-photo" role="img" aria-label="Photo of a silver sedan seen from the side"></div>

<section class="abs band">
  <svg class="abs" style="left:0;top:0" width="809" height="210" viewBox="0 0 809 210" fill="none" stroke="#fff" stroke-width="1.3">
    <polygon points="94,48 214,48 194,127 74,127"/>
    <polygon points="268,48 388,48 368,127 248,127"/>
    <polygon points="442,48 562,48 542,127 422,127"/>
    <polygon points="616,48 736,48 716,127 596,127"/>
    <g fill="#fff" stroke="none"><rect x="117" y="90" width="50" height="18" rx="4"/><path d="M121 90 L127 76 H142 V90 Z"/></g>
    <path d="M142 80 L163 62 V72" stroke-width="4"/>
    <circle cx="127" cy="110" r="6" fill="var(--red)" stroke-width="3"/><circle cx="157" cy="110" r="6" fill="var(--red)" stroke-width="3"/>
    <path d="M296 73 L312 66 L324 80 L336 70 L348 86" stroke-width="2"/>
    <g fill="#fff" stroke="none"><circle cx="296" cy="73" r="3"/><circle cx="312" cy="66" r="3"/><circle cx="324" cy="80" r="3"/><circle cx="336" cy="70" r="3"/><circle cx="348" cy="86" r="3"/></g>
    <path d="M454 100 L456 90 L470 87 L480 80 H500 L512 88 L528 91 L530 100 Z" fill="#fff" stroke="none"/>
    <circle cx="470" cy="100" r="5" fill="var(--red)" stroke-width="2"/><circle cx="518" cy="100" r="5" fill="var(--red)" stroke-width="2"/>
    <rect x="648" y="66" width="24" height="30" fill="#fff" stroke="none"/>
    <g stroke="var(--red)" stroke-width="2"><line x1="652" y1="73" x2="668" y2="73"/><line x1="652" y1="79" x2="668" y2="79"/></g>
    <circle cx="676" cy="98" r="13" fill="var(--red)" stroke-width="3"/>
    <text x="676" y="104" text-anchor="middle" fill="#fff" stroke="none" font-family="Roboto,Arial,sans-serif" font-weight="700" font-size="16">$</text>
  </svg>
  <div class="abs perk-label" style="left:65px;top:138px">Towing is Free</div>
  <div class="abs perk-label" style="left:239px;top:138px">Donations Accepted Nationwide</div>
  <div class="abs perk-label" style="left:407px;top:138px">All Vehicle Type Welcome</div>
  <div class="abs perk-label" style="left:582px;top:138px">Tax Deductible</div>
</section>

<section class="abs thanks">
  <h3>Thank You for Your Donation!</h3>
  <p>If you have any difficulty with this form or wish to speak with a representative immediately, then please</p>
  <div class="toll">Call us Toll-Free at 1-800-555-0147</div>
</section>

<footer class="abs footer">
  <div class="abs copyright">© Copyright 2017 Open Road Giving. All Rights Reserved.</div>
  <span class="abs social" style="left:611px"></span>
  <span class="abs social" style="left:640px"></span>
  <span class="abs social" style="left:668px"></span>
  <span class="abs social" style="left:697px"></span>
  <span class="abs social" style="left:726px"></span>
</footer>

</body>
</html>
```